Postcard Design January 2015

I need a postcard designed to introduce my company to potential new customers in the UK. My company is QT Page Solutions based in Chester and we represent one of Poland's leading and long established book printers. We offer competitive pricing, consistently high levels of print and binding quality and industry leading levels of customer service. We have been meeting the print requirements of UK publishers for more than 10 years.

```html
<!DOCTYPE html>
<html lang="en">
<head>
<meta charset="utf-8">
<title>QT Page Solutions – Postcard</title>
<link href="https://fonts.googleapis.com/css2?family=Arimo:wght@400;700&family=Oswald:wght@700&display=swap" rel="stylesheet">
<style>
  :root{
    --stage:#000000;
    --paper:#ffffff;
    --forest:#1a6b35;
    --lime:#4cb848;
    --accent:#f5e51a;
    --ink:#111111;
  }
  *{margin:0;padding:0;box-sizing:border-box}
  html,body{width:947px;height:1200px;overflow:hidden;background:var(--stage)}
  body{position:relative;font-family:"Arimo",Arial,sans-serif;color:var(--ink)}
  .card{position:absolute;background:var(--paper);overflow:hidden}
  .front{left:113px;top:34px;width:717px;height:556px}
  .back{left:113px;top:611px;width:720px;height:557px}

  /* front */
  .front-header{position:absolute;left:0;top:0;width:100%;height:130px;text-align:center}
  .brand-title{position:absolute;left:0;right:0;top:36px;font-weight:700;font-size:47px;letter-spacing:-0.5px;line-height:1}
  .brand-tagline{position:absolute;left:0;right:0;top:85px;font-size:26px;line-height:1;letter-spacing:-0.3px}
  .feature-band{position:absolute;left:0;top:130px;width:100%;height:349px;background:var(--forest);color:var(--paper)}
  .photo-grid{position:absolute;left:43px;top:25px;width:324px;height:307px}
  .photo{position:absolute}
  .photo-factory{left:0;top:0;width:175px;height:162px;background:linear-gradient(160deg,#c9ccd0,#7b8087 60%,#4d5158)}
  .photo-book{left:175px;top:0;width:149px;height:162px;background:linear-gradient(135deg,#5a5048,#d9d2c4 55%,#efe9dc)}
  .photo-foil{left:0;top:162px;width:175px;height:145px;background:linear-gradient(160deg,#e9e3d6,#d6cfc0 40%,#3d4f8c 60%,#b22a2a)}
  .photo-spines{left:175px;top:162px;width:149px;height:145px;background:linear-gradient(90deg,#2e2a29,#b53a30 30%,#e3d9c4 55%,#c94d2e 80%,#7a6a4a)}
  .headline{position:absolute;left:388px;top:28px;font-size:36px;line-height:38px;letter-spacing:-0.3px}
  .headline .highlight{color:var(--accent);font-weight:700}
  .pitch{position:absolute;left:390px;top:133px;width:310px;font-size:17px;line-height:20px}
  .front-cta{position:absolute;left:387px;top:284px;width:320px;font-size:18px;line-height:21px}
  .contact-strip{position:absolute;left:0;top:479px;width:100%;height:77px}
  .strip-slant{position:absolute;left:0;top:0;width:717px;height:77px}
  .phone-line{position:absolute;left:42px;top:14px;display:flex;align-items:center;gap:6px}
  .phone-number{font-family:"Oswald","Arial Narrow",sans-serif;font-weight:700;font-size:40px;line-height:1;letter-spacing:-1.5px}
  .web-line{position:absolute;left:390px;top:24px;display:flex;align-items:center;gap:12px;color:var(--paper);font-size:21px;letter-spacing:-0.2px}

  /* back */
  .info-panel{position:absolute;left:0;top:0;width:348px;height:331px;background:var(--forest);color:var(--paper);padding:32px 0 0 38px}
  .info-title{font-weight:700;font-size:22px;line-height:1;letter-spacing:-0.2px}
  .info-tagline{font-size:11px;margin-top:4px}
  .info-heading{font-weight:700;font-size:12px;margin-top:18px}
  .info-heading.spaced{margin-top:16px}
  .info-list{list-style:none;font-size:11.8px;line-height:16px;margin-top:1px;width:300px}
  .info-list li{padding-left:13px;text-indent:-13px}
  .building-photo{position:absolute;left:355px;top:35px;width:186px;height:139px;background:linear-gradient(180deg,#3d7fd0 0%,#9cc2ea 40%,#c8c9cb 62%,#6f6c69 100%)}
  .back-contact{position:absolute;left:38px;top:342px;font-size:14px;line-height:18px}
  .back-phone{position:absolute;left:37px;top:387px;font-size:19px}
  .back-web{position:absolute;left:38px;top:414px;font-size:14px;line-height:19px}
</style>
</head>
<body>

<section class="card front">
  <header class="front-header">
    <h1 class="brand-title">QT PAGE SOLUTIONS</h1>
    <p class="brand-tagline">Litho &amp; Digital Printing, BookBinding &amp; Finishing</p>
  </header>

  <div class="feature-band">
    <div class="photo-grid">
      <div class="photo photo-factory" role="img" aria-label="Photo of a book printing factory floor with binding lines"></div>
      <div class="photo photo-book" role="img" aria-label="Close-up photo of an open sewn book"></div>
      <div class="photo photo-foil" role="img" aria-label="Photo of hardback books with foil stamped covers"></div>
      <div class="photo photo-spines" role="img" aria-label="Photo of a row of colourful book spines"></div>
    </div>
    <h2 class="headline">BOOK PRINTING<br>MADE <span class="highlight">EASY</span></h2>
    <p class="pitch">We offer a truly competitive service to book publishers looking for excellence in book printing and binding, combined with a first rate service.</p>
    <p class="front-cta">Contact us for further information, quotations or samples.</p>
  </div>

  <div class="contact-strip">
    <svg class="strip-slant" viewBox="0 0 717 77" preserveAspectRatio="none" aria-hidden="true">
      <polygon points="394,77 471,0 717,0 717,77" fill="var(--lime)"/>
    </svg>
    <div class="phone-line">
      <svg width="26" height="44" viewBox="0 0 26 44" aria-hidden="true">
        <path d="M9 2 L15 2 L16 11 L11 13 C9 19 9 25 11 31 L16 33 L15 42 L9 42 C1 34 1 10 9 2 Z" fill="var(--ink)"/>
      </svg>
      <span class="phone-number">01244 550317</span>
    </div>
    <div class="web-line">
      <svg width="28" height="28" viewBox="0 0 28 28" aria-hidden="true" fill="none" stroke="var(--paper)" stroke-width="1.6">
        <circle cx="14" cy="14" r="12.5"/>
        <ellipse cx="14" cy="14" rx="5.5" ry="12.5"/>
        <line x1="14" y1="1.5" x2="14" y2="26.5"/>
        <line x1="1.5" y1="14" x2="26.5" y2="14"/>
        <path d="M3.5 7.5 H24.5 M3.5 20.5 H24.5"/>
      </svg>
      <span>www.qtpagesolutions.co.uk</span>
    </div>
  </div>
</section>

<section class="card back">
  <div class="info-panel">
    <h2 class="info-title">QT PAGE SOLUTIONS</h2>
    <p class="info-tagline">Litho &amp; Digital Printing, BookBinding &amp; Finishing</p>
    <h3 class="info-heading">SERVICES</h3>
    <ol class="info-list">
      <li>1. High quality book printing and binding</li>
      <li>2. Competitive pricing</li>
      <li>3. Excellent customer service</li>
    </ol>
    <h3 class="info-heading spaced">OTHER SERVICES</h3>
    <ol class="info-list">
      <li>1. We produce paperback and hardback books in mono or full colour. Binding options include &nbsp;sewn, perfect, Wiro-o and saddle stitched</li>
      <li>2. Print finishing includes lamination, spot UV and foil stamping</li>
      <li>3. We have state of the art production equipment, use top quality materials and follow strict quality control procedures</li>
      <li>4. We have weekly shipments in to the UK</li>
    </ol>
  </div>

  <div class="building-photo" role="img" aria-label="Photo of the printing plant building under a blue sky"></div>

  <p class="back-contact">Contact us for further<br>INFORMATION, QUOTATIONS or SAMPLES.</p>
  <p class="back-phone">Phone - 01244 550317</p>
  <p class="back-web">Website - www.qtpagesolutions.co.uk<br>Email - sam.hart@qtpagesolutions.co.uk</p>
</section>

</body>
</html>
```